Covid-19 Mortgage Housing Market Coaching

I need a one page 8.5 x 11 printable infographic to describe the following:
Housing and Mortgage Market Coach
Through your Employer Home-ownership Benefit
The Coronavirus has resulted in an unprecedented Government coordination to reduce the spread of the virus, as such, has altered the way we live and work.
As each of us looks to the potential impact of the Coronavirus to our financial stability, it can be difficult to obtain trusted information to help make sound financial decisions.
As part of your employee home ownership program through your employer, you have access to this educational coaching on the below topics:
• What is happening in the stock market and why it is happening.
• Motivation behind Feds cutting rates and how that translates to the lending market.
• Discuss the future of interest rates.
• Discuss the future of the housing market. How will the spring and summer housing markets be effected?
• Everyone says to refinance now. Is that really in my best interest? Learn how to do a refinance analysis and determine if refinancing is right for you.
Having a better understanding of what is happening in the financial markets, with interest rates and the housing market can help you successfully navigate this rapidly evolving situation.
Please be sure that our phone number is prominently displayed 1-800-529-8172 and our web address www.brightkeylending.example

```html
<!DOCTYPE html>
<html lang="en">
<head>
<meta charset="utf-8">
<title>Housing and Mortgage Market Coach</title>
<link href="https://fonts.googleapis.com/css2?family=Russo+One&family=Open+Sans:wght@400;600;700&display=swap" rel="stylesheet">
<style>
:root{
  --lime:#8cc63f;
  --lime-dark:#5f9a2c;
  --green:#24834a;
  --forest:#172b20;
  --ink:#1f3a2d;
  --white:#ffffff;
  --paper:#ffffff;
}
*{margin:0;padding:0;box-sizing:border-box}
html,body{width:928px;height:1200px;overflow:hidden;background:var(--paper)}
.sheet{position:relative;width:928px;height:1200px;overflow:hidden;background:var(--paper);font-family:"Open Sans",Arial,sans-serif}
.abs{position:absolute}
.band-dark{left:0;top:316px;width:928px;height:440px;background:var(--forest)}
.band-green{left:0;top:740px;width:928px;height:394px;background:var(--green)}
.footer-bar{left:0;top:1134px;width:928px;height:66px;background:var(--forest)}
.cloud{background:var(--lime);border-radius:60px}
.title{left:0;top:42px;width:928px;text-align:center;font-family:"Russo One",sans-serif;font-weight:400;font-size:54px;line-height:56px;color:var(--ink)}
.title span{display:inline-block;transform:scaleX(.8);transform-origin:center}
.ribbon{left:128px;top:160px;width:672px;height:70px}
.ribbon-text{left:161px;top:174px;width:602px;height:50px;display:flex;align-items:center;justify-content:center;font-weight:700;font-size:18px;color:var(--ink);letter-spacing:.3px}
.hero-art{left:44px;top:229px;width:468px;height:365px;border-radius:14px;background:linear-gradient(160deg,#9ad65a 0%,#5bb86a 40%,#d9d9d9 70%,#f4b183 100%)}
.intro{left:616px;width:282px;color:var(--white);font-size:15.5px;line-height:23px}
.intro em{font-style:normal;color:var(--lime)}
.intro-icon{left:496px;width:98px}
.card{left:33px;top:676px;width:861px;height:319px;background:var(--white);border-radius:16px}
.card-heading{left:98px;top:660px;width:747px;height:65px;background:var(--lime);border-radius:32px;display:flex;align-items:center;justify-content:center;text-align:center;font-weight:700;font-size:16px;line-height:22px;color:var(--ink)}
.topic{display:flex;align-items:flex-start;gap:16px;color:#222;font-size:15.5px;line-height:22px}
.topic svg{flex:none}
.closing{left:109px;top:1018px;width:580px;color:var(--white);font-size:15.5px;line-height:23px}
.bulb-art{left:708px;top:960px;width:118px;height:124px;border-radius:50% 50% 30% 30%;background:radial-gradient(circle at 50% 40%,#a7d964 0%,#8cc63f 55%,#24834a 100%)}
.brand-pill{left:0;top:1107px;width:251px;height:93px;background:var(--white);border-radius:0 46px 0 0;display:flex;align-items:center;gap:10px;padding-left:50px}
.brand-mark{width:16px;height:16px;background:var(--green)}
.brand-name{font-weight:700;font-size:17px;color:var(--green)}
.contact{left:371px;top:1134px;height:66px;display:flex;align-items:center;gap:14px;color:var(--white);font-weight:700;font-size:21px}
.contact .sep{font-weight:400;opacity:.8}
</style>
</head>
<body>
<div class="sheet">
  <div class="abs band-dark"></div>
  <div class="abs band-green"></div>
  <div class="abs footer-bar"></div>

  <div class="abs cloud" role="img" aria-label="Decorative green cloud" style="left:49px;top:55px;width:82px;height:70px"></div>
  <div class="abs cloud" role="img" aria-label="Decorative green cloud" style="left:800px;top:38px;width:128px;height:66px"></div>
  <div class="abs cloud" role="img" aria-label="Decorative green cloud" style="left:790px;top:220px;width:138px;height:96px;border-radius:70px 70px 0 0"></div>

  <h1 class="abs title"><span>HOUSING AND MORTGAGE</span><br><span>MARKET COACH</span></h1>

  <svg class="abs ribbon" viewBox="0 0 672 70" aria-hidden="true">
    <polygon points="0,0 50,0 50,54 0,54 14,27" fill="var(--lime-dark)"/>
    <polygon points="622,0 672,0 658,27 672,54 622,54" fill="var(--lime-dark)"/>
    <rect x="33" y="14" width="606" height="50" fill="var(--lime)"/>
  </svg>
  <div class="abs ribbon-text">THROUGH YOUR EMPLOYER HOME-OWNERSHIP BENEFIT</div>

  <div class="abs hero-art" role="img" aria-label="Illustration of a green-roofed house resting on an open hand"></div>

  <svg class="abs intro-icon" style="top:349px;height:93px" viewBox="0 0 98 93" aria-hidden="true">
    <g fill="none" stroke="var(--lime)" stroke-width="3">
      <circle cx="22" cy="40" r="14"/><circle cx="62" cy="24" r="18"/><circle cx="52" cy="72" r="12"/>
    </g>
    <g fill="var(--lime)"><circle cx="22" cy="40" r="5"/><circle cx="62" cy="24" r="6"/><circle cx="52" cy="72" r="4"/></g>
  </svg>
  <p class="abs intro" style="top:349px"><em>The Coronavirus</em> has resulted in an unprecedented Government coordination to reduce the spread of the virus, as such, has altered the way we live and work.</p>

  <svg class="abs intro-icon" style="top:496px;height:109px" viewBox="0 0 98 109" aria-hidden="true">
    <circle cx="28" cy="62" r="24" fill="none" stroke="var(--lime)" stroke-width="5"/>
    <text x="28" y="75" text-anchor="middle" font-family="Georgia,serif" font-style="italic" font-weight="700" font-size="34" fill="var(--lime)">i</text>
    <text x="72" y="88" text-anchor="middle" font-family="Open Sans,sans-serif" font-weight="700" font-size="82" fill="var(--lime)">$</text>
  </svg>
  <p class="abs intro" style="top:496px">As each of us looks to the potential impact of the Coronavirus to our financial stability, <em>it can be difficult to obtain trusted information</em> to help make sound financial decisions.</p>

  <div class="abs card"></div>
  <div class="abs card-heading">As part of your employee home ownership program through your employer,<br>you have access to this educational coaching on the below topics:</div>

  <div class="abs topic" style="left:87px;top:752px;width:330px">
    <svg width="54" height="48" viewBox="0 0 54 48" aria-hidden="true"><g fill="none" stroke="var(--forest)" stroke-width="2.5"><path d="M10 44h40M20 44V30M28 44V22M36 44V16M44 44V8M14 30l12-12 8 6 14-18"/><circle cx="10" cy="34" r="8"/></g></svg>
    <span>What is happening in the stock market and why it is happening.</span>
  </div>
  <div class="abs topic" style="left:87px;top:834px;width:330px">
    <svg width="54" height="40" viewBox="0 0 54 40" aria-hidden="true"><g fill="none" stroke="var(--forest)" stroke-width="2.5"><circle cx="6" cy="12" r="5"/><circle cx="6" cy="28" r="5"/><path d="M10 15l14 7M10 25l14-7M26 20h4M34 20h4"/></g><text x="44" y="32" text-anchor="middle" font-family="Open Sans,sans-serif" font-weight="700" font-size="32" fill="var(--forest)">$</text></svg>
    <span>Motivation behind Feds cutting rates and how that translates to the lending market.</span>
  </div>
  <div class="abs topic" style="left:87px;top:921px;width:330px">
    <svg width="54" height="36" viewBox="0 0 54 36" aria-hidden="true"><g fill="none" stroke="var(--forest)" stroke-width="2.5"><path d="M8 4v28h26M12 28l8-10 6 6 12-16M32 8h6v6"/></g><text x="14" y="14" font-family="Open Sans,sans-serif" font-weight="700" font-size="11" fill="var(--forest)">%</text></svg>
    <span>Discuss the future of interest rates.</span>
  </div>
  <div class="abs topic" style="left:458px;top:756px;width:370px">
    <svg width="82" height="64" viewBox="0 0 82 64" aria-hidden="true"><g fill="none" stroke="var(--forest)" stroke-width="2.5"><path d="M6 30L41 4l35 26M16 24v36h50V24M28 54V44M36 54V38M44 54V32M52 54V26M26 36l12-10 8 4 10-10"/></g></svg>
    <span>Discuss the future of the housing market. How will the spring and summer housing markets be effected?</span>
  </div>
  <div class="abs topic" style="left:458px;top:853px;width:370px">
    <svg width="82" height="64" viewBox="0 0 82 64" aria-hidden="true"><g fill="none" stroke="var(--forest)" stroke-width="2.5"><circle cx="38" cy="32" r="14"/><path d="M14 18h40l-6-6M68 46H28l6 6M8 26v20h18M74 38V18H58"/></g><text x="38" y="40" text-anchor="middle" font-family="Open Sans,sans-serif" font-weight="700" font-size="20" fill="var(--forest)">$</text></svg>
    <span>Everyone says to refinance now. Is that really in my best interest? Learn how to do a refinance analysis and determine if refinancing is right for you.</span>
  </div>

  <div class="abs bulb-art" role="img" aria-label="Icon of a head outline with a dollar lightbulb"></div>
  <p class="abs closing">Having a better understanding of what is happening in the financial markets, with interest rates and the housing market can help you successfully navigate this rapidly evolving situation.</p>

  <div class="abs brand-pill"><span class="brand-mark"></span><span class="brand-name">Brightkey Lending</span></div>

  <svg class="abs" style="left:281px;top:1110px" width="73" height="73" viewBox="0 0 73 73" aria-hidden="true">
    <circle cx="36.5" cy="36.5" r="33" fill="var(--forest)" stroke="var(--lime)" stroke-width="4"/>
    <path d="M24 18c3-2 6 0 8 4l2 5c1 3-1 5-3 6 2 5 5 8 10 10 1-2 3-4 6-3l5 2c4 2 6 5 4 8-3 5-9 7-15 4-10-5-17-12-21-22-2-6 0-12 4-14z" fill="var(--lime)"/>
  </svg>
  <div class="abs contact"><span>1-800-529-8172</span><span class="sep">|</span><span>www.brightkeylending.example</span></div>
</div>
</body>
</html>
```